SEO marketing site

I need a design only for an SEO/Marketing project I have in mind. I have bought the domain Brovelle.example and want to aim this project at businesses who want to push their business further. WHEN I SAY DESIGN ONLY, I MEAN NO PROGRAMMING. HOWEVER, I DO NEED THE DESIGNER TO PUT THIS SITE ONLINE. $300 IS A LOT OF MONEY FOR A TEMPLATE YOU CAN PURCHASE FOR $60 WITH SOME CUSTOMISATION.

The idea is that businesses will register with us and will be offered two different kinds of services. They can make use of our scripts to check their back links, rankings, compare with competitors and a number of other marketing tools. The other service we provide is that we offer them an SEO service at a very competitive price. We will handle social networking, link building, article submission, directory submission, social bookmarking etc etc at a reasonable monthly fee.

I quorix tiled look/flat design is what I really like, and I want to give off a professional vibe. This is the kind of site I wish to go for.

JUST TO REPEAT, I NEED A DESIGN TO BE PUT ONLINE, I.E PSD TO HTML CONVERSION. MY PROGRAMMERS WILL CODE THE CLIENT AREA THEMSELVES.

Target Market(s)

Other businesses

Industry/Entity Type

Marketing

Requirements
Must have
• Quorix 5 or flat design look. Even a site, similar to plumtower, is quite attractive. I would like a killer design for the site.

```html
<!DOCTYPE html>
<html lang="en">
<head>
<meta charset="utf-8">
<title>Brovelle.example — SEO &amp; Marketing</title>
<link rel="stylesheet" href="https://fonts.googleapis.com/css2?family=Montserrat:wght@400;500;600;700&family=Open+Sans:ital,wght@0,400;0,600;0,700;1,400&display=swap">
<style>
:root{
  --navy:#1d3a66;
  --navy-deep:#0b1a33;
  --blue:#2b4f86;
  --accent:#f5a623;
  --yellow:#f2e33a;
  --text:#555a60;
  --muted:#8a8f96;
  --line:#e3e5e8;
  --light:#f1f2f4;
  --white:#ffffff;
}
*{box-sizing:border-box;margin:0;padding:0}
html,body{width:1200px;height:2544px;overflow:hidden;background:var(--white)}
body{font-family:"Open Sans",Arial,sans-serif;color:var(--text);font-size:13px;line-height:1.62;position:relative}
h1,h2,h3,h4{font-family:"Montserrat",Arial,sans-serif;font-weight:600}
a{color:var(--blue);text-decoration:none}
.wrap{width:920px;margin:0 auto;position:relative}

/* top bar */
.topbar{height:28px;background:var(--light);font-size:13px}
.topbar .wrap{display:flex;justify-content:space-between;align-items:center;height:28px}
.topbar .call{font-weight:700;color:#6a6f76}
.topbar .call b{color:var(--blue)}
.topbar .auth{display:flex;gap:2px;height:28px}
.topbar .auth span{background:var(--blue);color:#fff;font-size:12px;padding:0 10px;display:flex;align-items:center;gap:5px}
.topbar .auth span.reg{background:#6c7f99}

/* header */
.header{height:84px}
.header .wrap{display:flex;justify-content:space-between;align-items:center;height:84px}
.logo{font-family:"Montserrat",sans-serif;font-weight:700;font-size:28px;color:var(--navy);letter-spacing:.5px}
.logo small{font-size:15px;color:#8fa0b8;font-weight:400}
.nav{display:flex;gap:10px;font-size:14px;color:#6a6f76}
.nav span{padding:3px 16px}
.nav .active{background:var(--blue);color:#fff}

/* hero */
.hero{height:418px;background:linear-gradient(180deg,#0e2243 0%,#142d55 60%,#0b1a33 100%);position:relative;overflow:hidden}
.hero .art{position:absolute;left:230px;top:40px;width:760px;height:378px;background:radial-gradient(ellipse at 50% 45%,#9fb6c8 0%,#5b7896 45%,rgba(20,45,85,0) 75%)}
.hero h2{position:absolute;left:148px;top:262px;font-size:40px;color:var(--yellow);font-weight:600}
.hero p{position:absolute;left:700px;top:274px;width:340px;color:#fff;font-size:13.5px;line-height:1.55}
.hero .arrow{position:absolute;top:152px}
.hero .arrow.l{left:72px}.hero .arrow.r{right:72px}

/* about */
.about{height:344px;padding-top:32px}
.section-title{font-size:24px;color:var(--navy);text-transform:uppercase;letter-spacing:.3px}
.about .text{width:530px;margin-top:10px;font-size:13.5px}
.about .text p+p{margin-top:14px}
.video{position:absolute;left:580px;top:50px;width:320px;height:212px;background:#fff;padding:8px;box-shadow:0 10px 22px rgba(0,0,0,.22)}
.video .screen{width:100%;height:100%;background:linear-gradient(135deg,#1b3048,#3f6580 55%,#1a2b40);display:flex;align-items:center;justify-content:center}

/* expertise */
.expertise{height:458px;background:linear-gradient(110deg,#3a1d42 0%,#2c2d5c 45%,#4a2a52 75%,#23264e 100%)}
.expertise .section-title{color:#fff;padding-top:22px}
.cards{display:flex;gap:29px;margin-top:20px}
.card{width:208px;height:348px;background:#fff;position:relative;box-shadow:0 6px 14px rgba(0,0,0,.35)}
.card h3{background:linear-gradient(#fdfdfd,#e2e4e7);height:68px;padding:10px 12px 0 26px;font-size:20px;line-height:1.05;color:#222;position:relative;font-weight:600}
.card h3::before{content:"";position:absolute;left:12px;top:10px;width:5px;height:46px;background:var(--blue)}
.card p{padding:16px 16px 0 18px;font-size:13.5px;color:#555;position:relative;z-index:1}
.card .foot{position:absolute;left:0;right:0;bottom:0;height:96px;background:linear-gradient(#fff,#eceef1)}

/* features */
.features{height:233px;border-bottom:1px solid var(--line)}
.features .wrap{display:flex;height:100%}
.feature{flex:1;padding:32px 20px 0;border-right:1px solid var(--line)}
.feature:first-child{padding-left:0}
.feature:last-child{border-right:0;padding-right:0}
.feature h3{display:flex;align-items:center;gap:20px;font-size:22px;color:var(--navy);font-weight:500;text-transform:uppercase}
.feature p{margin-top:20px;font-size:13.5px}

/* clients + blog */
.lower{height:407px;padding-top:28px}
.lower .wrap{display:flex;justify-content:space-between}
.clients{width:590px}
.bar-head{display:flex;justify-content:space-between;align-items:center}
.btn-view{background:#e8e9eb;color:#666;font-size:12px;padding:3px 14px}
.client-grid{display:grid;grid-template-columns:repeat(3,1fr);margin-top:20px}
.client{height:134px;display:flex;align-items:center;justify-content:center;gap:8px;font-family:"Open Sans",sans-serif;font-weight:700;font-size:22px;color:#7d8288}
.client:nth-child(-n+3){border-bottom:1px solid var(--line)}
.client:not(:nth-child(3n)){border-right:1px solid var(--line)}
.client i{width:14px;height:14px;background:#9aa0a6;border-radius:50%;display:block}
.blog{width:260px}
.post{display:flex;gap:16px;padding:18px 0 16px;border-bottom:1px solid var(--line)}
.date{width:66px;flex:none;text-align:center;background:#e8e9eb;font-family:"Montserrat",sans-serif;color:#555}
.date .tag{background:var(--accent);color:#fff;font-size:9px;height:15px;line-height:15px}
.date b{display:block;font-size:26px;line-height:1.1;margin-top:6px}
.date span{font-size:14px}
.post p{font-size:13px}
.post a{color:var(--accent)}
.blog .btn-view{display:block;text-align:center;margin-top:22px;padding:6px}

/* contact */
.contact{height:520px;background:linear-gradient(180deg,#05101f 0%,#0f2440 50%,#0b1a2e 100%);color:#fff;text-align:center;padding-top:24px}
.contact h2{font-size:26px;font-weight:600}
.contact .sub{font-style:italic;font-size:14px;margin-top:4px;color:#e6ecf4}
.contact .dots{width:460px;height:2px;margin:10px auto 0;background:linear-gradient(90deg,transparent,#3c5c85,transparent);position:relative}
.contact .dots::after{content:"";position:absolute;left:50%;top:-3px;width:8px;height:8px;border-radius:50%;background:#5b83b5;transform:translateX(-50%)}
.contact-row{display:flex;gap:21px;margin-top:38px;text-align:left}
.map{width:459px;height:258px;background:linear-gradient(135deg,#e9e4d6,#f4eed9 40%,#e0d9c4);border:4px solid #fff}
.enquiry{width:440px;height:258px;background:#fff;padding:14px 18px;color:#222}
.enquiry h3{font-size:24px;font-weight:600}
.fields{display:flex;gap:10px;margin-top:8px}
.field{flex:1;background:#e6e7e9;border:1px solid #d0d2d5;font-size:12px;color:#555;padding:3px 8px;height:28px}
.field.msg{height:96px;margin-top:10px}
.send{display:inline-block;background:var(--accent);color:#fff;font-family:"Montserrat",sans-serif;font-weight:600;font-size:18px;padding:2px 16px;margin-top:12px}
.info-row{display:flex;margin-top:26px;text-align:left}
.info{display:flex;gap:12px}
.info.loc{width:267px}
.info.tel{width:219px}
.info.mail{width:248px}
.info.web{flex:1}
.info h4{font-size:17px;font-weight:600;line-height:1.2}
.info p{font-size:13px;color:#c9d3e0;line-height:1.35}

/* footer */
.footer{height:52px}
.footer .wrap{display:flex;justify-content:space-between;align-items:center;height:52px;font-size:12px}
.social{display:flex;gap:5px}
.social span{width:30px;height:30px;background:var(--blue);display:block}
</style>
</head>
<body>

<div class="topbar"><div class="wrap">
  <div class="call">Information Call - <b>(800) 41 602 73314</b></div>
  <div class="auth">
    <span><svg width="11" height="11" viewBox="0 0 12 12"><rect x="2" y="5" width="8" height="7" fill="#fff"/><path d="M4 5V3.5a2 2 0 0 1 4 0V5" stroke="#fff" fill="none" stroke-width="1.4"/></svg>LOGIN</span>
    <span class="reg"><svg width="11" height="11" viewBox="0 0 12 12"><path d="M1 11l1-3 6-6 2 2-6 6z" fill="#fff"/></svg>REGISTER</span>
  </div>
</div></div>

<header class="header"><div class="wrap">
  <div class="logo">BROVELLE<small>.example</small></div>
  <nav class="nav"><span class="active">Home</span><span>About</span><span>Services</span><span>Clients</span><span>Blog</span><span>Contact</span></nav>
</div></header>

<section class="hero">
  <div class="art" role="img" aria-label="Isometric illustration of buildings on a hexagon grid linked by dotted arcs"></div>
  <svg class="arrow l" width="40" height="120" viewBox="0 0 40 120"><path d="M34 4L6 60l28 56" stroke="#8aa0bf" stroke-width="2" fill="none"/></svg>
  <svg class="arrow r" width="40" height="120" viewBox="0 0 40 120"><path d="M6 4l28 56-28 56" stroke="#8aa0bf" stroke-width="2" fill="none"/></svg>
  <h2>Link Building</h2>
  <p>Lorem Ipsum, Proin gravida nibh vel velit auctor aliquet. Aenean sollicitudin, lorem quis bibendum auctor, nisi elit consequat ipsum, nec sagittis sem nibh id elit.</p>
</section>

<section class="about"><div class="wrap">
  <h2 class="section-title">About Company</h2>
  <div class="text">
    <p>This is the studio version of Lorem Ipsum. Proin gravida nibh vel velit auctor aliquet. Aenean sollicitudin, lorem quis bibendum auctor, nisi elit consequat ipsum, nec sagittis sem nibh id elit. Duis sed odio sit amet nibh vulputate cursus a sit amet mauris. Morbi accumsan ipsum velit. Nam nec tellus a odio tincidunt auctor a ornare odio.</p>
    <p>Sed non mauris vitae erat consequat auctor eu in elit. Class aptent taciti sociosqu ad litora torquent per conubia nostra, per inceptos himenaeos. Mauris in erat justo. Nullam ac urna eu felis dapibus condimentum sit amet a augue. Sed non neque elit. Sed ut imperdiet nisi. Proin condimentum fermentum nunc. Etiam massa nisl quis neque. Suspendisse in orci enim.</p>
  </div>
  <div class="video"><div class="screen" role="img" aria-label="Video still of a hand touching a digital SEO interface">
    <svg width="64" height="64" viewBox="0 0 64 64"><circle cx="32" cy="32" r="30" fill="#fff" opacity=".92"/><path d="M25 19l21 13-21 13z" fill="#2a2f36"/></svg>
  </div></div>
</div></section>

<section class="expertise"><div class="wrap">
  <h2 class="section-title">Expertise</h2>
  <div class="cards">
    <div class="card"><h3>Social<br>Networking</h3><p>This is the studio version of Lorem Ipsum. Proin gravida nibh vel velit auctor aliquet. Aenean sollicitudin, lorem quis bibendum auctor, nisi elit consequat ipsum, nec selit...<a>Read more</a></p><div class="foot" role="img" aria-label="Faint illustration of social network icons"></div></div>
    <div class="card"><h3>Link<br>Building</h3><p>This is the studio version of Lorem Ipsum. Proin gravida nibh vel velit auctor aliquet. Aenean sollicitudin, lorem quis bibendum auctor, nisi elit consequat ipsum, nec selit...<a>Read more</a></p><div class="foot" role="img" aria-label="Faint illustration of a connected globe"></div></div>
    <div class="card"><h3>Article<br>Submission</h3><p>This is the studio version of Lorem Ipsum. Proin gravida nibh vel velit auctor aliquet. Aenean sollicitudin, lorem quis bibendum auctor, nisi elit consequat ipsum, nec selit...<a>Read more</a></p><div class="foot" role="img" aria-label="Faint illustration of a newspaper"></div></div>
    <div class="card"><h3>Directory<br>Submission</h3><p>This is the studio version of Lorem Ipsum. Proin gravida nibh vel velit auctor aliquet. Aenean sollicitudin, lorem quis bibendum auctor, nisi elit consequat ipsum, nec selit...<a>Read more</a></p><div class="foot" role="img" aria-label="Faint illustration of address cards"></div></div>
  </div>
</div></section>

<section class="features"><div class="wrap">
  <div class="feature"><h3><svg width="46" height="32" viewBox="0 0 46 32"><rect x="6" y="2" width="34" height="22" fill="#e4e6e9" stroke="#b9bec4"/><path d="M1 26h44l-3 4H4z" fill="#c8ccd1"/></svg>How It Works</h3><p>This is the studio version of Lorem Ipsum. Proin gravida nibh vel velit auctor aliquet. Aenean sollicitudin, lorem quis bibendum auctor, nisi elit consequat ipsum, nec selit...<a>Read more</a></p></div>
  <div class="feature"><h3><svg width="40" height="32" viewBox="0 0 40 32"><rect x="2" y="2" width="36" height="28" fill="#fff" stroke="#b9bec4" stroke-width="2"/><rect x="2" y="2" width="36" height="7" fill="#c8ccd1"/><rect x="7" y="14" width="12" height="10" fill="#e4e6e9"/></svg>Why Choose Us</h3><p>This is the studio version of Lorem Ipsum. Proin gravida nibh vel velit auctor aliquet. Aenean sollicitudin, lorem quis bibendum auctor, nisi elit consequat ipsum, nec selit...<a>Read more</a></p></div>
  <div class="feature"><h3><svg width="48" height="30" viewBox="0 0 48 30"><rect x="1" y="4" width="46" height="24" rx="3" fill="#e4e6e9" stroke="#b9bec4"/><g fill="#b9bec4"><rect x="6" y="9" width="5" height="4"/><rect x="14" y="9" width="5" height="4"/><rect x="22" y="9" width="5" height="4"/><rect x="30" y="9" width="5" height="4"/><rect x="38" y="9" width="5" height="4"/><rect x="10" y="19" width="28" height="4"/></g></svg>Our Vision</h3><p>This is the studio version of Lorem Ipsum. Proin gravida nibh vel velit auctor aliquet. Aenean sollicitudin, lorem quis bibendum auctor, nisi elit consequat ipsum, nec selit...<a>Read more</a></p></div>
</div></section>

<section class="lower"><div class="wrap">
  <div class="clients">
    <div class="bar-head"><h2 class="section-title">Clients</h2><span class="btn-view">View All</span></div>
    <div class="client-grid">
      <div class="client"><i></i>Quenmarro</div>
      <div class="client">Zelvuna</div>
      <div class="client">Dravik</div>
      <div class="client"><i></i>Halvoria</div>
      <div class="client">Morvessa</div>
      <div class="client">Tiberne</div>
    </div>
  </div>
  <div class="blog">
    <h2 class="section-title">Blog</h2>
    <div class="post"><div class="date"><div class="tag">Post</div><b>20</b><span>MAR</span></div><p>This is the studio version of Lorem Ipsum. Proin gravida nibh velor aliquet... <a>Read more</a></p></div>
    <div class="post"><div class="date"><div class="tag">Post</div><b>20</b><span>MAR</span></div><p>This is the studio version of Lorem Ipsum. Proin gravida nibh velor aliquet... <a>Read more</a></p></div>
    <span class="btn-view">View All</span>
  </div>
</div></section>

<section class="contact"><div class="wrap">
  <h2>CONTACT</h2>
  <div class="sub">Come on. We have introduced ourself much. Just leave a message.</div>
  <div class="dots"></div>
  <div class="contact-row">
    <div class="map" role="img" aria-label="Street map showing the office location"></div>
    <div class="enquiry">
      <h3>ENQUIRY</h3>
      <div class="fields"><div class="field">Enter Your Name :</div><div class="field">Enter Your Email :</div></div>
      <div class="field msg">Enter Your Message :</div>
      <span class="send">SEND</span>
    </div>
  </div>
  <div class="info-row">
    <div class="info loc"><svg width="20" height="26" viewBox="0 0 20 26"><path d="M10 1a9 9 0 0 0-9 9c0 7 9 15 9 15s9-8 9-15a9 9 0 0 0-9-9z" fill="#fff"/><circle cx="10" cy="10" r="3.5" fill="#0f2440"/></svg><div><h4>Location</h4><p>14, Larkin Row, Ellsworth,<br>402 Vantoria.</p></div></div>
    <div class="info tel"><svg width="18" height="28" viewBox="0 0 18 28"><rect x="1" y="1" width="16" height="26" rx="3" fill="#fff"/><rect x="3" y="4" width="12" height="17" fill="#0f2440"/></svg><div><h4>Phone :</h4><p>(800) 41 602 73314</p></div></div>
    <div class="info mail"><svg width="28" height="20" viewBox="0 0 28 20"><rect x="1" y="1" width="26" height="18" fill="#fff"/><path d="M1 1l13 10L27 1" stroke="#0f2440" stroke-width="2" fill="none"/></svg><div><h4>Email :</h4><p>hello@brovelle.example</p></div></div>
    <div class="info web"><svg width="30" height="26" viewBox="0 0 30 26"><rect x="1" y="1" width="28" height="18" fill="#fff"/><rect x="4" y="4" width="22" height="12" fill="#0f2440"/><rect x="11" y="20" width="8" height="3" fill="#fff"/><rect x="7" y="23" width="16" height="2" fill="#fff"/></svg><div><h4>Website :</h4><p>www.Brovelle.example</p></div></div>
  </div>
</div></section>

<footer class="footer"><div class="wrap">
  <span>Copyright © 2013 Brovelle.example All rights reserved</span>
  <div class="social"><span></span><span></span><span></span><span></span><span></span><span></span></div>
</div></footer>

</body>
</html>
```